Therapy Services & Training

I provide counseling/therapy to individuals and families. I also travel the country and provide training at conferences.
I would like to see a card which takes my company name and design a logo using the letters "HWAE".
Target Market(s)
Therapists, non-profit organizations, clients looking for therapy
Industry/Entity Type
Training
Contact Information for Business Card
Harborview Wellness Advising & Education LLC
Delia Marsh, M.S.W., LCSW
Clinical Therapist & Trainer
Providing clinical therapy services to individuals, families, couples & children. We also provide life coaching and crisis training.
counselordelia@mailbrook.net
www.harborviewwellnessadvising.com
(555) 214-3092
Millbrook, IL 60999
(BACK SIDE OF CARD)
We are certified by the Ongoing Professional Lawyer Studies (OPLS) Council of the Prairie High Tribunal to provide Continuing Legal Education (CLE) credits to Illinois attorneys. Call about what courses we offer! (555) 214-3092

```html
<!DOCTYPE html>
<html lang="en">
<head>
<meta charset="utf-8">
<title>Harborview Wellness Advising &amp; Education – Business Card</title>
<link rel="stylesheet" href="https://fonts.googleapis.com/css2?family=Oswald:wght@500;600&family=Arimo:wght@400;700&display=swap">
<style>
  :root {
    --backdrop: #e9e7e3;
    --paper: #ffffff;
    --blue-deep: #24389a;
    --blue-mid: #3f58bf;
    --blue-light: #8a9ddf;
    --blue-pale: #b7c3ee;
    --ink: #141414;
    --ink-soft: #3a3a3a;
    --phone-grey: #555a60;
  }
  * { box-sizing: border-box; margin: 0; padding: 0; }
  html, body { width: 1200px; height: 900px; overflow: hidden; }
  body {
    background: var(--backdrop);
    font-family: "Arimo", Arial, sans-serif;
    color: var(--ink);
    display: flex;
    flex-direction: column;
    align-items: center;
    justify-content: center;
    gap: 36px;
  }
  .card {
    position: relative;
    width: 700px;
    height: 400px;
    background: var(--paper);
    overflow: hidden;
    box-shadow: 0 6px 18px rgba(0,0,0,0.18);
  }
  .band-top {
    position: absolute; left: 0; right: 0; top: 0;
    background: linear-gradient(90deg, var(--blue-mid), var(--blue-light) 55%, var(--blue-pale));
  }
  .rule-top, .rule-bottom {
    position: absolute; left: 0; right: 0; height: 2px;
    background: var(--blue-deep);
  }
  .band-bottom {
    position: absolute; left: 0; right: 0; bottom: 0;
    background: linear-gradient(180deg, var(--blue-mid), var(--blue-deep));
  }

  /* Front */
  .front .band-top { height: 26px; }
  .front .rule-top { top: 33px; }
  .company-name {
    position: absolute; left: 30px; right: 30px; top: 48px;
    font-family: "Oswald", "Arial Narrow", sans-serif;
    font-weight: 600;
    font-size: 27px;
    line-height: 34px;
    letter-spacing: 0;
    text-transform: uppercase;
    color: var(--ink);
    white-space: nowrap;
  }
  .front .logo {
    position: absolute; left: 56px; top: 150px;
    font-family: "Arimo", Arial, sans-serif;
    font-weight: 700;
    font-size: 72px;
    color: var(--blue-mid);
    letter-spacing: 2px;
  }
  .contact-block { position: absolute; left: 390px; top: 118px; }
  .person-name { font-size: 28px; font-weight: 700; color: var(--ink-soft); }
  .credentials { font-size: 12px; color: var(--ink-soft); margin: 3px 0 12px; }
  .contact-list { list-style: none; }
  .contact-list li {
    display: flex; align-items: center; gap: 7px;
    font-size: 12.5px; color: var(--ink); line-height: 19px;
    white-space: nowrap;
  }
  .contact-list svg { width: 11px; height: 11px; fill: var(--blue-mid); flex: none; }
  .front .rule-bottom { bottom: 118px; }
  .front .band-bottom { height: 112px; }
  .tagline {
    position: absolute; left: 0; right: 0; bottom: 34px;
    text-align: center;
    color: var(--paper);
    font-size: 16px; font-weight: 700; line-height: 22px;
  }

  /* Back */
  .back .band-top { height: 44px; }
  .back .rule-top { top: 52px; }
  .back-message {
    position: absolute; left: 40px; right: 40px; top: 84px;
    text-align: center;
  }
  .certification { font-size: 17px; font-weight: 700; line-height: 23px; }
  .call-to-action { font-size: 15px; font-weight: 700; margin-top: 18px; }
  .back-phone { font-size: 25px; font-weight: 700; color: var(--phone-grey); margin-top: 4px; }
  .back .rule-bottom { bottom: 124px; }
  .back .band-bottom { height: 118px; }
  .back .logo {
    position: absolute; right: 70px; bottom: 24px;
    font-family: "Arimo", Arial, sans-serif;
    font-weight: 700;
    font-size: 72px;
    color: var(--paper);
    letter-spacing: 2px;
  }
</style>
</head>
<body>

  <section class="card front" aria-label="Business card front">
    <div class="band-top"></div>
    <div class="rule-top"></div>
    <h1 class="company-name">Harborview Wellness Advising &amp; Education LLC</h1>
    <div class="logo">HWAE</div>

    <div class="contact-block">
      <h2 class="person-name">Delia Marsh</h2>
      <p class="credentials">M.S.W., LCSW Clinical Therapist &amp; Trainer</p>
      <ul class="contact-list">
        <li><svg viewBox="0 0 24 24"><path d="M6.6 10.8a15 15 0 0 0 6.6 6.6l2.2-2.2a1 1 0 0 1 1-.25 11.4 11.4 0 0 0 3.6.57 1 1 0 0 1 1 1V20a1 1 0 0 1-1 1A17 17 0 0 1 3 4a1 1 0 0 1 1-1h3.5a1 1 0 0 1 1 1c0 1.25.2 2.45.57 3.6a1 1 0 0 1-.25 1z"/></svg>(555) 214-3092</li>
        <li><svg viewBox="0 0 24 24"><path d="M2 5h20v2l-10 7L2 7z"/><path d="M2 8l10 7 10-7v11H2z"/></svg>counselordelia@mailbrook.net</li>
        <li><svg viewBox="0 0 24 24"><circle cx="10" cy="10" r="6.5" fill="none" stroke="#3f58bf" stroke-width="3"/><path d="M14.5 14.5l6 6" stroke="#3f58bf" stroke-width="3.5"/></svg>www.harborviewwellnessadvising.com</li>
        <li><svg viewBox="0 0 24 24"><path d="M12 3l10 9h-3v9h-5v-6h-4v6H5v-9H2z"/></svg>Millbrook, IL 60999</li>
      </ul>
    </div>

    <div class="rule-bottom"></div>
    <div class="band-bottom"></div>
    <p class="tagline">Providing clinical therapy services to individuals, families, couples &amp; children.<br>We also provide life coaching and crisis training</p>
  </section>

  <section class="card back" aria-label="Business card back">
    <div class="band-top"></div>
    <div class="rule-top"></div>
    <div class="back-message">
      <p class="certification">We are certified by the Ongoing Professional Lawyer Studies (OPLS) Council of the Prairie High Tribunal to provide Continuing Legal Education (CLE) credits to Illinois attorneys.</p>
      <p class="call-to-action">Call about what courses we offer!</p>
      <p class="back-phone">(555) 214-3092</p>
    </div>
    <div class="rule-bottom"></div>
    <div class="band-bottom"></div>
    <div class="logo">HWAE</div>
  </section>

</body>
</html>
```